BENEATH THE [HARBOR] OF A DAWN, Mend your road

We are looking for a cover refresh of an existing bestselling book that is going into 3rd edition print this year.
The book is an inspirational as well as educational book that has become recognized as one of the most comprehensive, actionable, personal and financial planning resources available today for families, individuals and business owners alike.
Comprised of three true stories of loss, learning to live and love again and a 30 page checklist at the back of the book it contains tips and strategies for everyone to help them to get their personal and financial lives in order while they can.
The cover must have the following:
1. Appeal to a broad audience/both personal and corporate
2. Include Mara Quellton Bestselling Author
3. Include introduction of a new Afterword
4. 3rd Edition
5. Colors to remain the same – red, black and white
6. The title must remain in caps and the word [HARBOR] must have the brackets around it
We have also added a current copy of the second edition to help you. For your information our website is www.thequelltonhouse.example
Reason: We have narrowed it down to our top 3 designs. We are submitting the covers to our community for them to pick the top cover. Good luck to everyone

```html
<!DOCTYPE html>
<html lang="en">
<head>
<meta charset="utf-8">
<title>Beneath the [Harbor] of a Dawn — Cover</title>
<link rel="stylesheet" href="https://fonts.googleapis.com/css2?family=Josefin+Sans:wght@200;300;400&family=Cinzel:wght@400;600&display=swap">
<style>
  :root {
    --page-bg: #e6e6e6;
    --cover-light: #f1f1f1;
    --cover-mid: #d9d9d9;
    --wine: #6b1a1c;
    --ink: #1a1a1a;
    --paper-white: #ffffff;
  }
  html, body {
    margin: 0;
    padding: 0;
    width: 1200px;
    height: 927px;
    overflow: hidden;
    background: var(--page-bg);
  }
  .canvas {
    position: relative;
    width: 1200px;
    height: 927px;
  }
  .cover {
    position: absolute;
    left: 310px;
    top: 33px;
    width: 580px;
    height: 860px;
    overflow: hidden;
    background: radial-gradient(ellipse at 40% 40%, var(--cover-light) 0%, var(--cover-mid) 100%);
    box-shadow: 0 6px 24px rgba(0,0,0,0.18);
    font-family: "Josefin Sans", sans-serif;
  }
  .edition-band {
    position: absolute;
    inset: 0;
    width: 580px;
    height: 860px;
  }
  .edition-text {
    position: absolute;
    top: 24px;
    right: 24px;
    width: 290px;
    text-align: center;
    color: var(--paper-white);
    font-family: "Cinzel", serif;
  }
  .edition-number {
    font-size: 30px;
    font-weight: 600;
    letter-spacing: 1px;
    padding-bottom: 6px;
    border-bottom: 1px solid rgba(255,255,255,0.8);
  }
  .edition-number sup { font-size: 16px; }
  .edition-note {
    margin-top: 6px;
    font-size: 15px;
    line-height: 1.2;
    letter-spacing: 1px;
  }
  .title {
    position: absolute;
    left: 40px;
    top: 255px;
    width: 500px;
    margin: 0;
    font-weight: 400;
    color: var(--ink);
    text-transform: uppercase;
  }
  .title-lead {
    font-size: 40px;
    font-weight: 400;
    letter-spacing: 1px;
    line-height: 1;
  }
  .title-key {
    font-size: 104px;
    font-weight: 300;
    color: var(--wine);
    line-height: 0.95;
    letter-spacing: 2px;
  }
  .title-tail {
    font-size: 44px;
    font-weight: 400;
    text-align: right;
    line-height: 1;
    margin-top: -8px;
  }
  .tagline {
    position: absolute;
    left: 40px;
    top: 445px;
    width: 500px;
    text-align: center;
    font-size: 34px;
    font-weight: 200;
    color: var(--ink);
    letter-spacing: 2px;
  }
  .nib-photo {
    position: absolute;
    left: 260px;
    top: 500px;
    width: 320px;
    height: 230px;
    background: linear-gradient(120deg, rgba(214,170,70,0) 0%, #c9a04a 30%, #8c6a2a 55%, #2a2a2a 75%, #111 100%);
  }
  .author {
    position: absolute;
    left: 150px;
    top: 750px;
    width: 390px;
    white-space: nowrap;
  }
  .author-name {
    font-size: 36px;
    font-weight: 400;
    color: var(--wine);
    letter-spacing: 2px;
    line-height: 1.1;
    text-transform: uppercase;
    padding-bottom: 4px;
    border-bottom: 1px solid var(--ink);
  }
  .author-role {
    margin-top: 6px;
    font-size: 22px;
    line-height: 1.1;
    color: var(--ink);
    letter-spacing: 2px;
    text-transform: uppercase;
  }
</style>
</head>
<body>
<div class="canvas">
  <section class="cover">
    <svg class="edition-band" viewBox="0 0 580 860" aria-hidden="true">
      <polygon points="60,0 580,0 580,260" fill="var(--wine)"/>
    </svg>
    <div class="edition-text">
      <div class="edition-number">3<sup>RD</sup> Edition</div>
      <div class="edition-note">INTRODUCTION OF A<br>NEW AFTERWORD</div>
    </div>

    <h1 class="title">
      <div class="title-lead">Beneath the</div>
      <div class="title-key">[Harbor]</div>
      <div class="title-tail">of a Dawn</div>
    </h1>
    <div class="tagline">- Mend Your Road -</div>

    <div class="nib-photo" role="img" aria-label="Close-up photograph of a gold fountain pen nib on a dark pen body"></div>

    <div class="author">
      <div class="author-name">Mara Quellton</div>
      <div class="author-role">Bestselling Author</div>
    </div>
  </section>
</div>
</body>
</html>
```